Business card for a "family office" company

Please provide professional looking business card designs, incorporating the attached logo and below details. Harrowmere Holdings Pty Ltd is a family office / financial investment company. We are looking for a modern, professional and contemporary card design.

Industry/Entity Type

Finance

Contact Information for Business Card

Name: Dean Malcott
Title: Director
Company: Harrowmere Holdings Pty Ltd
Email: harrowlead@ozmailnet.com.au
Mobile: 0492 635 718
Address: 3/412 Bramwood Parade, Kellmore Bay WA 6998, Australia

Requirements
Must have
• All details above and the logo. logo only on back side. incorporate colours of logo
Nice to have
• up to you
Should not have
• ?

```html
<!DOCTYPE html>
<html lang="en">
<head>
<meta charset="utf-8">
<title>Harrowmere Holdings – Business Card</title>
<link rel="stylesheet" href="https://fonts.googleapis.com/css2?family=Open+Sans:wght@400;600;700&display=swap">
<style>
  :root {
    --backdrop: #d9dadd;
    --navy: #1c1f5e;
    --band-blue: #2a3896;
    --paper: #f7f7f8;
    --white: #ffffff;
    --ink-light: #e8eaf4;
  }
  * { margin: 0; padding: 0; box-sizing: border-box; }
  html, body {
    width: 1200px; height: 960px; overflow: hidden;
    background: var(--backdrop);
    font-family: "Open Sans", Arial, sans-serif;
  }
  .canvas {
    width: 1200px; height: 960px;
    display: flex; flex-direction: column;
    align-items: center; justify-content: center; gap: 64px;
  }
  .card {
    width: 580px; height: 354px; position: relative; overflow: hidden;
    border-radius: 3px;
    box-shadow: 0 6px 18px rgba(0,0,0,.18);
  }
  /* Back side */
  .card-back {
    background: var(--navy);
    display: flex; align-items: center; justify-content: center;
  }
  .wordmark {
    display: flex; align-items: center; gap: 14px;
    font-weight: 600; letter-spacing: 3px; text-transform: uppercase;
  }
  .wordmark-square { width: 22px; height: 22px; }
  .card-back .wordmark { color: var(--white); font-size: 27px; }
  .card-back .wordmark-square { background: var(--white); }

  /* Front side */
  .card-front {
    background: var(--paper);
    display: flex; flex-direction: column;
  }
  .front-logo-area {
    height: 180px; display: flex; align-items: flex-end; justify-content: center;
    padding-bottom: 22px;
  }
  .card-front .wordmark { color: var(--navy); font-size: 25px; }
  .card-front .wordmark-square { background: var(--navy); }
  .name-band {
    height: 38px; background: var(--band-blue);
    display: flex; align-items: center; justify-content: center;
    color: var(--white); font-size: 15px; letter-spacing: .3px;
  }
  .name-band .person { font-weight: 700; text-transform: uppercase; }
  .name-band .role { font-weight: 400; text-transform: uppercase; margin-left: 4px; }
  .rule { height: 2px; background: var(--white); opacity: .9; }
  .front-details {
    flex: 1; background: var(--navy);
    display: flex; align-items: flex-start; justify-content: center;
  }
  .contact-block {
    text-align: center; color: var(--ink-light);
    font-size: 13px; line-height: 19px; padding-top: 16px;
  }
  .contact-block .company { font-weight: 700; color: var(--white); }
</style>
</head>
<body>
  <main class="canvas">
    <section class="card card-back" aria-label="Card back">
      <div class="wordmark">
        <span class="wordmark-square"></span>
        <span class="wordmark-name">Harrowmere Holdings</span>
      </div>
    </section>

    <section class="card card-front" aria-label="Card front">
      <div class="front-logo-area">
        <div class="wordmark">
          <span class="wordmark-square"></span>
          <span class="wordmark-name">Harrowmere Holdings</span>
        </div>
      </div>
      <div class="name-band">
        <span class="person">Dean Malcott</span>
        <span class="role">- Director</span>
      </div>
      <div class="rule"></div>
      <div class="front-details">
        <div class="contact-block">
          <p class="company">Harrowmere Holdings Pty Ltd</p>
          <p>3/412 Bramwood Parade, Kellmore Bay WA 6998, Australia</p>
          <p>M: 0492 635 718 &nbsp;E : harrowlead@ozmailnet.com.au</p>
          <p>W : harrowmereholdings.com.au</p>
        </div>
      </div>
    </section>
  </main>
</body>
</html>
```